Business card for psychiatrist

Business card design project for a psychiatristWe would like to have the impression of 1. We (patient and the doctor) are working together.2. Light the way so that patients can see where they are going and what their goals are.3. One side of the business card will have the letter "BFP" which stands for Brynmoor Family Psychiatry.4. The other side of the business card will have the address, phone number, name of the psychiatrist, website, etc.5. A logo could go into either side of the business card. Let's see what looks better.
Business card design project for a psychiatrist
We would like to have the impression of
1. We (patient and the doctor) are working together.
2. Light the way so that patients can see where they are going and what their goals are.
3. One side of the business card will have the letter "BFP" which stands for Brynmoor Family Psychiatry.
4. The other side of the business card will have the address, phone number, name of the psychiatrist, website, etc.
5. A logo could go into either side of the business card. Let's see what looks better.

```html
<!DOCTYPE html>
<html lang="en">
<head>
<meta charset="utf-8">
<title>Brynmoor Family Psychiatry – Business Card</title>
<link rel="stylesheet" href="https://fonts.googleapis.com/css2?family=Cinzel:wght@400;500&family=Open+Sans:wght@400&display=swap">
<style>
  :root {
    --page-bg: #e9e5e1;
    --card-white: #ffffff;
    --card-brown: #5b4a45;
    --ink-brown: #4a3b36;
    --leaf-green: #8cc540;
    --text-grey: #3d3d3d;
    --soft-cream: #f2ede8;
  }
  * { margin: 0; padding: 0; box-sizing: border-box; }
  html, body {
    width: 1200px;
    height: 900px;
    overflow: hidden;
    background: var(--page-bg);
  }
  .canvas {
    position: relative;
    width: 1200px;
    height: 900px;
  }
  .card {
    position: absolute;
    left: 250px;
    width: 700px;
    height: 400px;
    box-shadow: 0 6px 18px rgba(0,0,0,0.18);
  }
  .card--back {
    top: 40px;
    background: var(--card-brown);
    display: flex;
    align-items: center;
    justify-content: center;
  }
  .card--front {
    top: 465px;
    background: var(--card-white);
  }
  .brand {
    display: flex;
    align-items: center;
    gap: 14px;
  }
  .brand__dot {
    width: 26px;
    height: 26px;
    border-radius: 50%;
    background: var(--leaf-green);
    flex: none;
  }
  .brand__name {
    font-family: "Cinzel", serif;
    font-weight: 500;
    font-size: 30px;
    line-height: 1.15;
    letter-spacing: 1px;
  }
  .card--back .brand__name { color: var(--soft-cream); }
  .card--front .brand {
    position: absolute;
    left: 50px;
    top: 150px;
    width: 300px;
  }
  .card--front .brand__name { color: var(--ink-brown); font-size: 27px; }
  .contact {
    position: absolute;
    left: 410px;
    top: 115px;
  }
  .contact__name {
    font-family: "Cinzel", serif;
    font-size: 30px;
    font-weight: 400;
    color: var(--ink-brown);
    letter-spacing: 1px;
  }
  .contact__title {
    font-family: "Cinzel", serif;
    font-size: 19px;
    color: var(--leaf-green);
    letter-spacing: 1px;
    margin-bottom: 22px;
  }
  .contact__line {
    display: flex;
    align-items: flex-start;
    gap: 10px;
    font-family: "Open Sans", sans-serif;
    font-size: 17px;
    color: var(--text-grey);
    line-height: 1.75;
  }
  .contact__icon {
    width: 14px;
    height: 18px;
    margin-top: 6px;
    flex: none;
  }
  .contact__icon--blank { visibility: hidden; }
</style>
</head>
<body>
<main class="canvas">
  <section class="card card--back">
    <div class="brand">
      <span class="brand__dot"></span>
      <span class="brand__name">Brynmoor Family Psychiatry</span>
    </div>
  </section>

  <section class="card card--front">
    <div class="brand">
      <span class="brand__dot"></span>
      <span class="brand__name">Brynmoor Family Psychiatry</span>
    </div>

    <div class="contact">
      <h1 class="contact__name">YOUR NAME</h1>
      <p class="contact__title">JOB TITLE</p>
      <p class="contact__line">
        <svg class="contact__icon" viewBox="0 0 14 18" aria-hidden="true">
          <path d="M3 1 L6 1 L7 5 L5 6.5 Q6 10 8.5 12 L10 10.5 L13 12 L12.5 16 Q5 16 2 8 Q1.5 4 3 1 Z" fill="var(--leaf-green)"/>
        </svg>
        <span>000 000 0000</span>
      </p>
      <p class="contact__line">
        <svg class="contact__icon" viewBox="0 0 14 18" aria-hidden="true">
          <path d="M7 1 A6 6 0 0 1 13 7 C13 11 7 17 7 17 C7 17 1 11 1 7 A6 6 0 0 1 7 1 Z" fill="var(--leaf-green)"/>
          <circle cx="7" cy="7" r="2.3" fill="var(--card-white)"/>
        </svg>
        <span>418 Alder Lane</span>
      </p>
      <p class="contact__line">
        <span class="contact__icon contact__icon--blank"></span>
        <span>Westbrook, MD 21044</span>
      </p>
    </div>
  </section>
</main>
</body>
</html>
```